Tanwick Services Website Design

We have most content but require a professional design. We have a logo already and will need it utilized along with several of the photos from the attached documentation.
First page should have our mission and Vision and the synapsis provided in the word document. Visitors will be prompted to select from one of our 3 divisions from this page.
Each division will have the same list of tabs : About, Services, Safety, Careers and Contact.
Photos on each divisions page should be representative of the divisions offerings. The word doc attached contains the requested content and we are open to edits that would complement and fill the website.
I like the Morvalix site www.morvalix-demo.net - they are our competition so cant be modeled directly after this.
Please include prompts to request quote at each service page. align the format of the geotechnical page to the other 2 divisions.
I used chat gpt for some of the content so will need it optimized for SCO.

```html
<!DOCTYPE html>
<html lang="en">
<head>
<meta charset="utf-8">
<title>Tanwick Services – Home</title>
<link href="https://fonts.googleapis.com/css2?family=Montserrat:wght@400;500;600;700;800&display=swap" rel="stylesheet">
<style>
:root{
  --red:#e11b22;
  --ink:#1c1c1c;
  --muted:#4a4a4a;
  --white:#ffffff;
  --canvas:#f2f2f2;
  --dark:#121110;
  --field:#ffffff;
}
*{box-sizing:border-box;margin:0;padding:0}
html,body{width:1200px;height:900px;overflow:hidden;background:var(--canvas);font-family:"Montserrat",sans-serif;color:var(--ink)}
.stage{position:relative;width:1200px;height:900px}
.page{position:absolute;left:376px;top:3px;width:780px;height:1555px;transform:scale(.575);transform-origin:0 0;background:var(--white);box-shadow:0 10px 50px rgba(0,0,0,.18);overflow:hidden}

/* nav */
.nav{height:40px;display:flex;align-items:center;justify-content:space-between;padding:0 38px}
.brand{font-weight:800;font-size:15px;letter-spacing:1px;color:var(--red)}
.menu{display:flex;align-items:center;gap:32px;font-size:12px;color:var(--ink)}
.menu .active{color:var(--red);text-decoration:underline;text-underline-offset:3px;font-weight:600}
.menu .caret{font-size:7px;vertical-align:middle}
.menu .cta{background:var(--red);color:var(--white);padding:3px 12px;border-radius:2px;margin-left:-4px}

/* hero */
.hero{position:relative;height:400px;text-align:center;color:var(--white)}
.hero-photo{position:absolute;inset:0;background:linear-gradient(180deg,#4f6a80 0%,#8b8a84 28%,#5a5a56 55%,#1e1d1c 85%,#111 100%)}
.hero-inner{position:relative;padding-top:112px}
.hero .welcome{font-size:19px;font-weight:700;letter-spacing:.5px}
.hero .wordmark{font-size:54px;font-weight:800;letter-spacing:4px;color:var(--red);line-height:1;margin-top:4px}
.hero .lede{font-size:11px;line-height:13px;margin:16px auto 0;width:330px}
.divisions{position:absolute;left:216px;top:260px;width:347px;height:102px;background:var(--white);border-radius:2px;display:flex;align-items:center;color:var(--ink)}
.division{flex:1;display:flex;flex-direction:column;align-items:center;font-size:11.5px;font-weight:500;line-height:16px}
.division svg{width:26px;height:30px;margin-bottom:8px}
.division + .division{border-left:1px solid #777;height:50px;justify-content:flex-end}
.division:first-child{height:50px;justify-content:flex-end}
.division + .division svg{margin-top:-36px}

/* vision */
.about{height:385px;text-align:center;padding-top:38px}
.section-title{display:inline-flex;align-items:center;gap:10px;color:var(--red);font-weight:700;font-size:20px;letter-spacing:.3px}
.section-title::before,.section-title::after{content:"";width:22px;height:2px;background:var(--red)}
.about p{font-size:10.5px;line-height:13px;color:var(--ink);margin:20px auto 0}
.about .vision{width:420px}
.about .mission{width:460px}
.about .gap{height:38px}
.actions{display:flex;justify-content:center;gap:9px;margin-top:30px}
.btn{font-size:12px;font-weight:500;padding:7px 16px;border:1px solid var(--ink);border-radius:2px;background:var(--white)}
.btn.outline{border-color:var(--red);color:var(--red);padding:7px 9px}

/* careers */
.careers{position:relative;height:260px;text-align:center;color:var(--white)}
.careers-photo{position:absolute;inset:0;background:radial-gradient(ellipse at 70% 45%,#2e2a18 0%,#161512 55%,#0d0d0d 100%)}
.careers-inner{position:relative;padding-top:38px}
.careers h2{color:var(--red);font-size:19.5px;font-weight:700;letter-spacing:.3px}
.careers .sub{font-size:11px;margin-top:12px}
.form{width:347px;margin:20px auto 0;display:grid;grid-template-columns:1fr 1fr;gap:10px 8px}
.field{height:30px;background:var(--field);border-radius:2px;text-align:left;font-size:10px;color:#888;padding:9px 12px}
.subscribe{display:inline-block;margin-top:13px;background:var(--red);color:var(--white);font-size:12px;font-weight:600;padding:8px 21px;border-radius:2px}

/* testimonials */
.clients{height:250px;text-align:center;padding-top:34px}
.clients h2{color:var(--red);font-size:19.5px;font-weight:700}
.carousel{display:flex;align-items:center;justify-content:center;gap:15px;margin-top:18px}
.arrow{width:22px;height:22px;border-radius:50%;border:1px solid #ddd;font-size:11px;line-height:20px;color:var(--ink);margin:0 25px}
.avatar{width:50px;height:50px;border-radius:50%;background:radial-gradient(circle at 50% 40%,#9a8d80 0%,#5d5752 60%,#3a3836 100%)}
.quote{font-size:7.5px;line-height:10px;color:var(--muted);width:230px;margin:22px auto 0}
.name{font-size:11px;font-weight:700;margin-top:18px}
.role{font-size:6px;color:var(--muted);margin-top:2px}

/* footer */
.footer{position:absolute;left:38px;top:1336px;width:703px;height:177px;color:var(--white)}
.footer-photo{position:absolute;inset:0;background:linear-gradient(90deg,#120f0c 0%,#2a231b 55%,#15120f 100%)}
.footer-brand{position:absolute;left:41px;top:40px;font-size:20px;font-weight:800;letter-spacing:1.5px;color:var(--red)}
.socials{position:absolute;left:41px;top:77px;display:flex;gap:16px}
.socials span{width:20px;height:20px;border-radius:50%;background:var(--white)}
.address{position:absolute;left:228px;top:40px;font-size:10.5px;line-height:13px}
.email{position:absolute;left:228px;top:84px;font-size:10.5px}
.links{position:absolute;left:412px;top:42px;display:grid;grid-template-columns:113px 88px auto;row-gap:30px;font-size:12px;font-weight:500}
.links .caret{font-size:7px;vertical-align:middle}
.legal{position:absolute;left:0;right:0;top:136px;text-align:center;font-size:6.5px;font-weight:600;line-height:15px}
</style>
</head>
<body>
<div class="stage">
  <div class="page">

    <header class="nav">
      <div class="brand">TANWICK</div>
      <nav class="menu">
        <span class="active">Home</span>
        <span>Services <span class="caret">▼</span></span>
        <span>Safety</span>
        <span>Careers</span>
        <span>About</span>
        <span class="cta">Contact</span>
      </nav>
    </header>

    <section class="hero">
      <div class="hero-photo" role="img" aria-label="Wind turbines and an industrial plant silhouetted against a cloudy dusk sky"></div>
      <div class="hero-inner">
        <div class="welcome">WELCOME TO</div>
        <div class="wordmark">TANWICK</div>
        <p class="lede">Tanwick Services: Delivering safe, reliable aerial access and maintenance services to Oil&amp;Gas, Construction, Utility, &amp; Renewable energy industries.</p>
      </div>
      <div class="divisions">
        <div class="division">
          <svg viewBox="0 0 26 30" fill="none" stroke="var(--red)" stroke-width="2">
            <path d="M4 26h18M6 26v-5h14v5M10 21l6-17M16 4l3 3"/><circle cx="8" cy="27" r="1.5" fill="var(--red)"/><circle cx="18" cy="27" r="1.5" fill="var(--red)"/>
          </svg>
          <span>Aerial</span><span>Access</span>
        </div>
        <div class="division">
          <svg viewBox="0 0 26 30" fill="none" stroke="var(--red)" stroke-width="2">
            <path d="M6 2v24M3 8h6M6 14l6 4M10 20h13v6H10zM13 20v-3h6v3"/><circle cx="13" cy="27" r="1.5" fill="var(--red)"/><circle cx="20" cy="27" r="1.5" fill="var(--red)"/>
          </svg>
          <span>Geotechnical</span><span>Drilling</span>
        </div>
        <div class="division">
          <svg viewBox="0 0 26 30" fill="none" stroke="var(--red)" stroke-width="2">
            <circle cx="13" cy="15" r="11"/><circle cx="13" cy="15" r="6"/><circle cx="13" cy="15" r="2" fill="var(--red)"/>
          </svg>
          <span>Renewable</span><span>Energy</span>
        </div>
      </div>
    </section>

    <section class="about">
      <h2 class="section-title">OUR VISION</h2>
      <p class="vision">To be the leading provider of aerial access, geotechnical drilling, and service solutions, setting the standard for excellence in safety, efficiency, and environmental stewardship.</p>
      <div class="gap"></div>
      <h2 class="section-title">MISSION STATEMENT</h2>
      <p class="mission">At Tanwick, our mission is to deliver unparalleled aerial access, geotechnical drilling, and service and maintenance solutions, consistently exceeding our clients' expectations. We strive to achieve this by investing in cutting-edge technology, fostering a culture of safety and continuous improvement, and prioritizing environmental sustainability. Through collaboration, integrity, and dedication, we aim to contribute to the success of our clients while maintaining the highest standards of quality and professionalism.</p>
      <div class="actions">
        <span class="btn">Know more</span>
        <span class="btn outline">Explore our services</span>
      </div>
    </section>

    <section class="careers">
      <div class="careers-photo" role="img" aria-label="Dimly lit photo of a worker in a hard hat and hi-vis gear on site"></div>
      <div class="careers-inner">
        <h2>NOW YOU CAN JOIN OUR TEAM &nbsp;AND START YOUR CAREER</h2>
        <p class="sub">Subscribe to know available positions and receive our news</p>
        <div class="form">
          <div class="field">First name</div>
          <div class="field">Last name</div>
          <div class="field">Business mail</div>
          <div class="field">Job title</div>
        </div>
        <span class="subscribe">Subscribe</span>
      </div>
    </section>

    <section class="clients">
      <h2>WHAT CLIENT SAY</h2>
      <div class="carousel">
        <span class="arrow">‹</span>
        <span class="avatar" role="img" aria-label="Client portrait"></span>
        <span class="avatar" role="img" aria-label="Client portrait"></span>
        <span class="avatar" role="img" aria-label="Client portrait"></span>
        <span class="avatar" role="img" aria-label="Client portrait"></span>
        <span class="avatar" role="img" aria-label="Client portrait"></span>
        <span class="arrow">›</span>
      </div>
      <p class="quote">Lorem ipsum dolor sit amet, consectetur adipisicing elit, sed do eiusmod tempor incididunt ut labore et dolore magna aliqua. Ut enim ad minim veniam, quis nostrud exercitation</p>
      <div class="name">JONAS VELDER</div>
      <div class="role">CEO Brightfield Eco</div>
    </section>

    <footer class="footer">
      <div class="footer-photo" role="img" aria-label="Dark photo of wind turbines and a crane at dusk"></div>
      <div class="footer-brand">TANWICK</div>
      <div class="socials"><span></span><span></span><span></span><span></span></div>
      <div class="address">218 Ridgeline Road<br>Harlow Bend AB T9X-4K2</div>
      <div class="email">info@tanwick-demo.net</div>
      <div class="links">
        <span>Services <span class="caret">▼</span></span><span>News</span><span>About</span>
        <span>Careers</span><span>Safety</span><span>Contact</span>
      </div>
      <div class="legal">
        Copyright 2024 tanwick &nbsp;| &nbsp;All rights reserved<br>
        Cookies Policy &nbsp;| &nbsp;Privacy Policy &nbsp;| &nbsp;Terms of Service
      </div>
    </footer>

  </div>
</div>
</body>
</html>
```